Low Testosterone Center Postcard Design

I need a jumbo direct mail marketing postcard for my men's low testosterone center. We evaluate and treat men with symptoms related to low testosterone. See my website www.harborvitalclinic.com for more info on the symptoms of low testosterone and the benefits from bio identical replacement therapy. We have physician oversight for our program. Images and documents are available on my website.

Industry/Entity Type

Marketing

```html
<!DOCTYPE html>
<html lang="en">
<head>
<meta charset="utf-8">
<title>Harbor Vital Clinic – TRT Postcard</title>
<link rel="stylesheet" href="https://fonts.googleapis.com/css2?family=Jost:wght@400;500;600;700&display=swap">
<style>
  :root {
    --backdrop: #5f5f61;
    --card: #ffffff;
    --brand-blue: #0a6fba;
    --accent-orange: #f5a728;
    --ink: #1d1d1f;
    --ink-soft: #3c3c3e;
    --check-red: #c8202f;
    --rule: #333333;
    --photo-light: #f4efec;
    --photo-warm: #d9b39c;
  }
  * { margin: 0; padding: 0; box-sizing: border-box; }
  html, body { width: 1200px; height: 809px; overflow: hidden; }
  body { background: var(--backdrop); font-family: "Jost", Arial, sans-serif; color: var(--ink); }

  .postcard { position: absolute; left: 52px; top: 52px; width: 1096px; height: 705px; background: var(--card); }

  .hero-panel { position: absolute; left: 14px; top: 21px; width: 287px; height: 307px; background: var(--brand-blue); padding: 62px 0 0 25px; }
  .hero-line { font-weight: 500; text-transform: uppercase; line-height: 1.19; }
  .hero-line--white { color: #fff; font-size: 28.5px; }
  .hero-line--orange { color: var(--accent-orange); font-size: 31px; line-height: 1.38; margin-top: 3px; }

  .hero-photo { position: absolute; left: 14px; top: 328px; width: 287px; height: 292px;
    background: linear-gradient(100deg, var(--photo-warm) 0%, var(--photo-light) 45%, var(--photo-warm) 100%); }

  .benefits { position: absolute; left: 342px; top: 40px; width: 340px; }
  .benefits-title { font-size: 28px; font-weight: 600; line-height: 1.1; }
  .benefits-lead, .benefits-intro { font-size: 13px; line-height: 20px; color: var(--ink-soft); }
  .benefits-intro { margin-top: 19px; }
  .benefit-list { list-style: none; margin-top: 18px; }
  .benefit-list li { font-size: 15px; font-weight: 600; line-height: 19.7px; display: flex; align-items: center; gap: 5px; }
  .benefit-list svg { width: 13px; height: 13px; flex: none; }

  .brand { position: absolute; left: 333px; top: 492px; width: 160px; text-align: center; }
  .brand-mark { width: 88px; height: 88px; border-radius: 50%; background: var(--accent-orange); margin: 0 auto 10px; }
  .brand-name { font-size: 17px; font-weight: 600; line-height: 1.15; color: var(--ink); text-transform: uppercase; }

  .divider { position: absolute; left: 507px; top: 486px; width: 1px; height: 124px; background: var(--rule); }

  .cta { position: absolute; left: 525px; top: 497px; }
  .cta-heading { color: var(--brand-blue); font-size: 21px; font-weight: 600; line-height: 25px; text-transform: uppercase; }
  .cta-phone { font-size: 29px; font-weight: 400; margin-top: 9px; line-height: 1.1; letter-spacing: 0.5px; }
  .cta-web { font-size: 16px; font-weight: 500; text-transform: uppercase; margin-top: 2px; }

  .mail-address { position: absolute; left: 715px; top: 42px; font-size: 18px; line-height: 20px; }
  .stamp-box { position: absolute; left: 969px; top: 33px; width: 93px; height: 106px; border: 1px solid var(--rule); }
</style>
</head>
<body>
<main class="postcard">
  <section class="hero-panel">
    <p class="hero-line hero-line--white">We can make<br>the difference</p>
    <p class="hero-line hero-line--orange">In how you<br>feel about<br>yourself</p>
  </section>
  <div class="hero-photo" role="img" aria-label="Photo of a smiling couple sharing a strawberry"></div>

  <section class="benefits">
    <h1 class="benefits-title">Benefits of TRT</h1>
    <p class="benefits-lead">What are the Benefits of TRT<br>(Testosterone Replacement Therapy)?</p>
    <p class="benefits-intro">Benefits of TRT (Testosterone Replacement Therapy) at Harbor Vital Clinic vary based upon the pre-therapy low testosterone symptoms and other factors, but can include:</p>
    <ul class="benefit-list">
      <li><svg viewBox="0 0 12 12"><path d="M1 6.5 L4.5 10 L11 1.5" fill="none" stroke="var(--check-red)" stroke-width="1.6"/></svg>Improved muscle mass and strength</li>
      <li><svg viewBox="0 0 12 12"><path d="M1 6.5 L4.5 10 L11 1.5" fill="none" stroke="var(--check-red)" stroke-width="1.6"/></svg>Increased energy and vitality</li>
      <li><svg viewBox="0 0 12 12"><path d="M1 6.5 L4.5 10 L11 1.5" fill="none" stroke="var(--check-red)" stroke-width="1.6"/></svg>Increased bone mineral density</li>
      <li><svg viewBox="0 0 12 12"><path d="M1 6.5 L4.5 10 L11 1.5" fill="none" stroke="var(--check-red)" stroke-width="1.6"/></svg>Improved sexual desire and performance</li>
      <li><svg viewBox="0 0 12 12"><path d="M1 6.5 L4.5 10 L11 1.5" fill="none" stroke="var(--check-red)" stroke-width="1.6"/></svg>Boosted energy</li>
      <li><svg viewBox="0 0 12 12"><path d="M1 6.5 L4.5 10 L11 1.5" fill="none" stroke="var(--check-red)" stroke-width="1.6"/></svg>Decreased irritability and depression</li>
      <li><svg viewBox="0 0 12 12"><path d="M1 6.5 L4.5 10 L11 1.5" fill="none" stroke="var(--check-red)" stroke-width="1.6"/></svg>Improved concentration and focus</li>
      <li><svg viewBox="0 0 12 12"><path d="M1 6.5 L4.5 10 L11 1.5" fill="none" stroke="var(--check-red)" stroke-width="1.6"/></svg>Improved motivation</li>
      <li><svg viewBox="0 0 12 12"><path d="M1 6.5 L4.5 10 L11 1.5" fill="none" stroke="var(--check-red)" stroke-width="1.6"/></svg>Decreased body fat</li>
      <li><svg viewBox="0 0 12 12"><path d="M1 6.5 L4.5 10 L11 1.5" fill="none" stroke="var(--check-red)" stroke-width="1.6"/></svg>Better mood</li>
      <li><svg viewBox="0 0 12 12"><path d="M1 6.5 L4.5 10 L11 1.5" fill="none" stroke="var(--check-red)" stroke-width="1.6"/></svg>Improved erectile function.</li>
    </ul>
  </section>

  <div class="brand">
    <div class="brand-mark"></div>
    <p class="brand-name">Harbor Vital Clinic</p>
  </div>
  <div class="divider"></div>

  <section class="cta">
    <p class="cta-heading">Make an<br>appointment now</p>
    <p class="cta-phone">609-555-0187</p>
    <p class="cta-web">www.harborvitalclinic.com</p>
  </section>

  <address class="mail-address" style="font-style:normal">240 Linden St. Suite<br>B&nbsp; Milford,&nbsp; NJ</address>
  <div class="stamp-box"></div>
</main>
</body>
</html>
```